Web Design Project and logo

We need a new web design and logo for www.kq7ventra.com

It is a mobile app development company. Site needs to look very cool/trendy as does the new logo.

Looking for the design (uncoded) and the logo file that my developers can then use to build out the site.

An example of a nice competitor site is www.plumwirestudio.com

We want something that looks fresh, clean and hip.

Also development of business cards.

Target Market(s)

Small to mid sized companies

Industry/Entity Type

Business

Requirements
Must have
• Ability to request a quote
Should look very trendy like www.plumwirestudio.com as an example of a competitor site

```html
<!DOCTYPE html>
<html lang="en">
<head>
<meta charset="utf-8">
<title>Make an enquiry – kq7</title>
<link href="https://fonts.googleapis.com/css2?family=Open+Sans:wght@300;400;700&family=Arimo:wght@400;700&display=swap" rel="stylesheet">
<style>
  :root {
    --page-bg: #ffffff;
    --topbar-bg: #ececec;
    --topbar-line: #d6d6d6;
    --heading: #333333;
    --body-text: #222222;
    --form-bg: #f7f7f7;
    --field-border: #cfcfcf;
    --field-bg: #ffffff;
    --button-top: #66bdf0;
    --button-bottom: #2b85d4;
    --button-text: #ffffff;
    --footer-bg: #3b3b3b;
    --footer-text: #ffffff;
    --social-circle: #a9aaac;
    --brand-circle: #eeeeee;
  }
  * { box-sizing: border-box; margin: 0; padding: 0; }
  html, body {
    width: 1200px; height: 811px; overflow: hidden;
    background: var(--page-bg);
  }
  .page { position: relative; width: 1200px; height: 811px; overflow: hidden; }

  .topbar {
    position: absolute; left: 0; top: 0; width: 1200px; height: 23px;
    background: var(--topbar-bg);
    border-bottom: 1px solid var(--topbar-line);
  }

  .enquiry-title {
    position: absolute; left: 0; top: 85px; width: 1164px;
    text-align: center;
    font-family: "Open Sans", sans-serif; font-weight: 700; font-size: 24px;
    color: var(--heading);
  }
  .enquiry-intro {
    position: absolute; left: 0; top: 154px; width: 1154px;
    text-align: center;
    font-family: Arimo, Arial, sans-serif; font-size: 14px;
    color: var(--body-text);
  }

  .enquiry-form {
    position: absolute; left: 437px; top: 219px; width: 298px; height: 303px;
    background: var(--form-bg);
  }
  .field-label {
    position: absolute; left: 25px;
    font-family: Arimo, Arial, sans-serif; font-weight: 700; font-size: 14px;
    color: var(--body-text);
  }
  .field-label span { font-weight: 400; }
  .field-input {
    position: absolute; left: 25px; width: 245px; height: 44px;
    background: var(--field-bg);
    border: 1px solid var(--field-border); border-radius: 4px;
  }
  .submit-button {
    position: absolute; left: 109px; top: 246px; width: 161px; height: 42px;
    border: none; border-radius: 21px;
    background: linear-gradient(to bottom, var(--button-top), var(--button-bottom));
    box-shadow: 0 1px 2px rgba(0,0,0,0.2);
    color: var(--button-text);
    font-family: "Open Sans", sans-serif; font-weight: 700; font-size: 18px;
    line-height: 38px; padding: 0;
  }

  .site-footer {
    position: absolute; left: 0; top: 618px; width: 1200px; height: 193px;
    background: var(--footer-bg); overflow: hidden;
  }
  .follow-title {
    position: absolute; left: 121px; top: 29px;
    font-family: "Open Sans", sans-serif; font-weight: 400; font-size: 18px;
    color: var(--footer-text);
  }
  .social-links { position: absolute; left: 123px; top: 93px; }
  .social-link {
    position: absolute; top: 0; width: 53px; height: 53px; border-radius: 50%;
    background: var(--social-circle);
  }
  .brand {
    position: absolute; left: 960px; top: 96px;
    display: flex; align-items: center; gap: 12px;
  }
  .brand-dot {
    width: 28px; height: 28px; border-radius: 50%;
    background: var(--brand-circle);
  }
  .brand-name {
    font-family: "Open Sans", sans-serif; font-weight: 700; font-size: 30px;
    line-height: 1; color: var(--footer-text);
  }
</style>
</head>
<body>
<div class="page">
  <div class="topbar"></div>

  <h1 class="enquiry-title">Make an enquiry</h1>
  <p class="enquiry-intro">Interested in App Management? Call 13000 48 517 or enquire below.</p>

  <form class="enquiry-form">
    <label class="field-label" style="top:10px">NAME <span>*</span></label>
    <div class="field-input" style="top:32px"></div>
    <label class="field-label" style="top:89px">EMAIL <span>*</span></label>
    <div class="field-input" style="top:111px"></div>
    <label class="field-label" style="top:168px">PHONE <span>*</span></label>
    <div class="field-input" style="top:190px"></div>
    <button type="button" class="submit-button">Enquire now</button>
  </form>

  <footer class="site-footer">
    <div class="follow-title">FOLLOW US</div>
    <div class="social-links">
      <a class="social-link" style="left:0" aria-label="Social link 1"></a>
      <a class="social-link" style="left:66px" aria-label="Social link 2"></a>
      <a class="social-link" style="left:131px" aria-label="Social link 3"></a>
      <a class="social-link" style="left:194px" aria-label="Social link 4"></a>
    </div>
    <div class="brand">
      <span class="brand-dot"></span>
      <span class="brand-name">kq7</span>
    </div>
  </footer>
</div>
</body>
</html>
```